Website for a Construction Business That Builds Houses

We want some design concepts for this website. Customer likes this competitor site: https://brenwickdwellings.com.au/

We have a logo for Tarvond Constructions. Logo font is Birdman, attached with AI.

Want to be able to change hero images

Will have a contact page.

Need to know what plugins will be used for WordPress.

Coding

Coded - Design and coding required

```html
<!DOCTYPE html>
<html lang="en">
<head>
<meta charset="utf-8">
<title>Tarvond Innovations — Home Builders</title>
<link href="https://fonts.googleapis.com/css2?family=Audiowide&family=Poppins:ital,wght@0,400;0,500;0,600;0,700;1,400&display=swap" rel="stylesheet">
<style>
:root{
  --green:#7ac143;
  --green-dark:#5f9f2f;
  --ink:#2b2b2b;
  --muted:#555;
  --topbar:#333333;
  --footer:#1b1b1b;
  --band:#efefef;
  --mint:#eef4e4;
  --white:#ffffff;
}
*{box-sizing:border-box;margin:0;padding:0}
html,body{width:1200px;height:3145px;overflow:hidden}
body{position:relative;font-family:"Poppins",sans-serif;color:var(--ink);background:var(--white)}
.abs{position:absolute}
.display{font-family:"Audiowide",sans-serif;font-weight:400}

/* top bar */
.topbar{left:0;top:0;width:1200px;height:30px;background:var(--topbar);color:#fff;font-size:15px}
.topbar .item{top:6px;display:flex;align-items:center;gap:8px}
.topbar svg{width:14px;height:14px}
.social{right:112px;top:8px;display:flex;gap:10px}
.social span{width:12px;height:12px;border-radius:50%;background:var(--green)}

/* header */
.header{left:0;top:30px;width:1200px;height:97px;background:var(--white)}
.brand{left:108px;top:30px;width:122px;height:132px;border-radius:0 0 61px 61px;background:var(--white);z-index:3;display:flex;flex-direction:column;align-items:center;justify-content:center;gap:4px;color:var(--ink);font-weight:600;text-align:center}
.brand .dot{width:34px;height:34px;border-radius:50%;background:var(--green)}
.brand .name{font-size:17px;line-height:1.1}
.nav{top:73px;left:564px;display:flex;gap:27px;font-size:15px;color:#333}
.nav .active{font-weight:600;position:relative}
.nav .active::before{content:"";position:absolute;left:12px;top:-12px;width:20px;height:4px;border-radius:2px;background:var(--green)}
.btn{display:inline-flex;align-items:center;justify-content:center;border-radius:24px;font-weight:600;font-size:15px;color:#fff}
.cta{left:955px;top:62px;width:133px;height:45px;background:var(--green)}

/* hero */
.hero{left:0;top:127px;width:1200px;height:428px;background:linear-gradient(180deg,#9cc3e4 0%,#b8cfd9 30%,#8a8175 48%,#6b6f5d 62%,#4f8a34 80%,#69a83a 100%)}
.hero-small{left:111px;top:340px;font-size:34px;color:#fff}
.hero-big{left:111px;top:380px;font-size:62px;color:#fff;line-height:1}
.hero-btn{left:116px;top:452px;width:132px;height:43px;background:#2e2e2e;font-size:15px}

/* section headings */
.heading{font-size:44px;color:#2a2a2a}
.heading-bar{width:78px;height:8px;background:var(--green);border-radius:4px}

/* who we are */
.about-shadow{left:133px;top:652px;width:313px;height:358px;background:#ececec}
.about-main{left:111px;top:631px;width:313px;height:359px;background:linear-gradient(180deg,#7fa8d8 0%,#b6c3cf 45%,#8a7a68 70%,#4f7d35 100%)}
.about-inset{left:288px;top:848px;width:244px;height:199px;background:linear-gradient(180deg,#6c7177 0%,#dfe3e6 45%,#a9acae 75%,#6d6e6f 100%)}
.about-title{left:617px;top:630px}
.about-bar{left:619px;top:690px}
.about-lead{left:617px;top:730px;width:460px;font-size:17px;font-weight:500;line-height:28px}
.about-lead em{font-style:normal;color:var(--green)}
.about-body{left:617px;top:792px;width:470px;font-size:15.5px;line-height:27.5px;color:var(--muted)}
.about-btn{left:618px;top:986px;width:134px;height:45px;background:var(--green)}

/* services */
.band{left:0;width:1200px;background:var(--band)}
.services{top:1115px;height:632px}
.svc-title{left:0;width:1200px;top:1168px;text-align:center}
.svc-bar{left:449px;top:1228px}
.card{top:1292px;width:309px;height:375px;overflow:hidden}
.card .label{position:absolute;left:33px;bottom:46px;color:#fff;font-weight:600;font-size:16.5px;line-height:28px;text-transform:uppercase}
.card .shade{position:absolute;left:0;right:0;bottom:0;height:150px;background:linear-gradient(180deg,rgba(0,0,0,0),rgba(0,0,0,.78))}
.card .corner{position:absolute;right:0;bottom:0;width:0;height:0;border-left:70px solid transparent;border-bottom:70px solid var(--green)}
.c1{left:111px;background:linear-gradient(180deg,#b9d4ef 0%,#f2f2f0 40%,#8d7a5a 75%,#3b3a33 100%)}
.c2{left:444px;background:linear-gradient(180deg,#7d8fae 0%,#4e5a75 45%,#b48e5d 72%,#3f3f40 100%)}
.c3{left:779px;background:linear-gradient(180deg,#7fa66a 0%,#806a5c 35%,#d9a6c5 62%,#6a7a4a 100%)}
.arrow{width:32px;height:32px;border-radius:50%;border:1.5px solid #333;display:flex;align-items:center;justify-content:center}
.arrow svg{width:14px;height:14px}
.arrow.faint{border-color:#9a9a9a}

/* testimonials */
.testi-title{left:0;width:1200px;top:1822px;text-align:center}
.testi-bar{left:481px;top:1882px}
.testi-box{left:111px;top:1978px;width:977px;height:295px;background:var(--mint)}
.quote{left:564px;top:1941px;width:72px;height:72px;border-radius:50%;background:var(--green);border:5px solid #dbe9c8;display:flex;align-items:center;justify-content:center;color:#fff;font-family:Georgia,serif;font-size:46px;font-weight:700;line-height:1;padding-top:14px}
.stars{left:0;width:1200px;top:2045px;display:flex;justify-content:center;gap:3px}
.stars svg{width:20px;height:20px}
.testi-text{left:230px;top:2077px;width:740px;text-align:center;font-style:italic;font-size:17.5px;line-height:34px;color:#333}
.testi-name{left:0;width:1200px;top:2206px;text-align:center;font-weight:500;font-size:17px}
.t-arrow{width:58px;height:58px;border-radius:50%;background:#fff;border:1px solid #ddd;display:flex;align-items:center;justify-content:center}
.t-arrow svg{width:16px;height:16px}

/* portfolio */
.portfolio{top:2368px;height:558px}
.pf-title{left:0;width:1200px;top:2420px;text-align:center}
.pf-bar{left:457px;top:2480px}
.shot{top:2550px;height:288px}
.p0{left:0;width:65px;background:linear-gradient(180deg,#4c5c7a,#8a7a68 60%,#5d5d5d)}
.p1{left:111px;width:296px;background:linear-gradient(180deg,#4a64a8 0%,#8d8fbf 40%,#d9d6dc 65%,#5b6b96 100%)}
.p2{left:452px;width:296px;background:linear-gradient(180deg,#6e9bd4 0%,#a9c3de 35%,#8a5e47 62%,#6a8a45 100%)}
.p3{left:793px;width:297px;background:linear-gradient(180deg,#5c6478 0%,#9ba1ad 35%,#3a3430 60%,#d9a24a 85%,#3d342d 100%)}
.p4{left:1135px;width:65px;background:linear-gradient(180deg,#4d7fd0,#b9c3cf 50%,#4f8f3a)}
.w-arrow{width:52px;height:52px;border-radius:50%;background:#fff;display:flex;align-items:center;justify-content:center;box-shadow:0 2px 6px rgba(0,0,0,.08)}
.w-arrow svg{width:14px;height:14px}

/* footer */
.footer{left:0;top:2926px;width:1200px;height:219px;background:var(--footer);color:#fff}
.f-brand{left:113px;top:2958px;display:flex;flex-direction:column;align-items:flex-start;gap:6px;font-weight:600;font-size:18px;color:#fff}
.f-brand .dot{width:36px;height:36px;border-radius:50%;background:var(--green)}
.f-col{top:2963px;font-size:16px;line-height:26px}
.f-col .k{text-transform:uppercase}
.f-icon{top:2966px;width:22px;height:22px}
.f-rule{left:111px;top:3068px;width:977px;height:1px;background:#444}
.copy{left:0;width:1200px;top:3093px;text-align:center;font-size:15px}
</style>
</head>
<body>

<!-- top bar -->
<div class="abs topbar">
  <div class="abs item" style="left:112px">
    <svg viewBox="0 0 24 24" fill="var(--green)"><path d="M6.6 10.8a15 15 0 0 0 6.6 6.6l2.2-2.2a1 1 0 0 1 1-.25 11.4 11.4 0 0 0 3.6.57 1 1 0 0 1 1 1V20a1 1 0 0 1-1 1A17 17 0 0 1 3 4a1 1 0 0 1 1-1h3.5a1 1 0 0 1 1 1c0 1.25.2 2.45.57 3.57a1 1 0 0 1-.25 1z"/></svg>
    +1 555-010-2040
  </div>
  <div class="abs item" style="left:290px">
    <svg viewBox="0 0 24 24" fill="var(--green)"><path d="M3 5h18v14H3z" opacity=".9"/><path d="M3 5l9 7 9-7" stroke="#333" stroke-width="2" fill="none"/></svg>
    info@tarvond.com
  </div>
  <div class="abs social" aria-label="Social links"><span></span><span></span><span></span></div>
</div>

<!-- header -->
<div class="abs header"></div>
<div class="abs brand"><span class="dot"></span><span class="name">Tarvond<br>Innovations</span></div>
<nav class="abs nav">
  <span class="active">Home</span><span>About</span><span>Sevices</span><span>Why Us</span><span>Contact</span>
</nav>
<div class="abs btn cta">Get Started</div>

<!-- hero -->
<div class="abs hero" role="img" aria-label="Large brick family home with double garage and green lawn"></div>
<div class="abs display hero-small">welcome to</div>
<div class="abs display hero-big">tarvond innovations</div>
<div class="abs btn hero-btn">Our Project</div>

<!-- who we are -->
<div class="abs about-shadow"></div>
<div class="abs about-main" role="img" aria-label="Two-storey suburban house lit at dusk"></div>
<div class="abs about-inset" role="img" aria-label="Bright open-plan living room seen from a deck"></div>
<h2 class="abs display heading about-title">who we are</h2>
<div class="abs heading-bar about-bar"></div>
<p class="abs about-lead">From <em>foundations to final touches</em>, we bring your dream home to life.</p>
<p class="abs about-body">We are a dedicated team of construction professionals specializing in building high-quality homes that meet the diverse needs of our clients. With years of experience and a commitment to excellence, we ensure every project is completed with the utmost precision, from the initial design to the final nail.</p>
<div class="abs btn about-btn">Learn More</div>

<!-- services -->
<div class="abs band services"></div>
<h2 class="abs display heading svc-title">our services</h2>
<div class="abs heading-bar svc-bar"></div>
<div class="abs arrow faint" style="left:34px;top:1462px"><svg viewBox="0 0 24 24" fill="none" stroke="#9a9a9a" stroke-width="2.5"><path d="M15 5l-7 7 7 7"/></svg></div>
<div class="abs card c1" role="img" aria-label="Modern white custom-built home">
  <div class="shade"></div><div class="label">Custom Home<br>Construction</div>
</div>
<div class="abs card c2" role="img" aria-label="Renovated two-storey home with lit windows">
  <div class="shade"></div><div class="corner"></div><div class="label">Renovations and<br>Remodeling</div>
</div>
<div class="abs card c3" role="img" aria-label="Country house framed by flowering shrubs">
  <div class="shade"></div><div class="label">Project<br>Management</div>
</div>
<div class="abs arrow" style="left:1128px;top:1462px"><svg viewBox="0 0 24 24" fill="none" stroke="#333" stroke-width="2.5"><path d="M9 5l7 7-7 7"/></svg></div>

<!-- testimonials -->
<h2 class="abs display heading testi-title">testimonials</h2>
<div class="abs heading-bar testi-bar"></div>
<div class="abs testi-box"></div>
<div class="abs quote">”</div>
<div class="abs stars" aria-label="Five stars">
  <svg viewBox="0 0 24 24" fill="#f5b301"><path d="M12 2l3 6.5 7 .8-5.2 4.8 1.4 7L12 17.6 5.8 21l1.4-7L2 9.3l7-.8z"/></svg>
  <svg viewBox="0 0 24 24" fill="#f5b301"><path d="M12 2l3 6.5 7 .8-5.2 4.8 1.4 7L12 17.6 5.8 21l1.4-7L2 9.3l7-.8z"/></svg>
  <svg viewBox="0 0 24 24" fill="#f5b301"><path d="M12 2l3 6.5 7 .8-5.2 4.8 1.4 7L12 17.6 5.8 21l1.4-7L2 9.3l7-.8z"/></svg>
  <svg viewBox="0 0 24 24" fill="#f5b301"><path d="M12 2l3 6.5 7 .8-5.2 4.8 1.4 7L12 17.6 5.8 21l1.4-7L2 9.3l7-.8z"/></svg>
  <svg viewBox="0 0 24 24" fill="#f5b301"><path d="M12 2l3 6.5 7 .8-5.2 4.8 1.4 7L12 17.6 5.8 21l1.4-7L2 9.3l7-.8z"/></svg>
</div>
<p class="abs testi-text">The team exceeded our expectations. Our new home is everything we envisioned and more. Professional, reliable, and skilled. We couldn't be happier with the results.</p>
<div class="abs testi-name">Dana Colwell</div>
<div class="abs t-arrow" style="left:81px;top:2102px"><svg viewBox="0 0 24 24" fill="none" stroke="#999" stroke-width="2"><path d="M15 5l-7 7 7 7"/></svg></div>
<div class="abs t-arrow" style="left:1059px;top:2102px"><svg viewBox="0 0 24 24" fill="none" stroke="#222" stroke-width="2.5"><path d="M9 5l7 7-7 7"/></svg></div>

<!-- portfolio -->
<div class="abs band portfolio"></div>
<h2 class="abs display heading pf-title">our portfolio</h2>
<div class="abs heading-bar pf-bar"></div>
<div class="abs shot p0" role="img" aria-label="Edge of a blue-sided house"></div>
<div class="abs shot p1" role="img" aria-label="Contemporary glass house reflected in a pool at dusk"></div>
<div class="abs shot p2" role="img" aria-label="Red-brick family home under blue sky"></div>
<div class="abs shot p3" role="img" aria-label="Modern home with glowing windows at sunset"></div>
<div class="abs shot p4" role="img" aria-label="Edge of a house with green lawn"></div>
<div class="abs w-arrow" style="left:34px;top:2668px"><svg viewBox="0 0 24 24" fill="none" stroke="#222" stroke-width="3"><path d="M15 5l-7 7 7 7"/></svg></div>
<div class="abs w-arrow" style="left:1107px;top:2668px"><svg viewBox="0 0 24 24" fill="none" stroke="#222" stroke-width="3"><path d="M9 5l7 7-7 7"/></svg></div>

<!-- footer -->
<footer class="abs footer"></footer>
<div class="abs f-brand"><span class="dot"></span><span>Tarvond<br>Innovations</span></div>

<svg class="abs f-icon" style="left:348px" viewBox="0 0 24 24" fill="none" stroke="#fff" stroke-width="1.6"><path d="M12 22s7-7 7-12a7 7 0 0 0-14 0c0 5 7 12 7 12z"/><circle cx="12" cy="10" r="2.5"/></svg>
<div class="abs f-col" style="left:389px"><div class="k">Address</div>Tarvond Innovations,<br>address comes here</div>

<svg class="abs f-icon" style="left:608px" viewBox="0 0 24 24" fill="none" stroke="#fff" stroke-width="1.6"><rect x="3" y="5" width="18" height="14" rx="1"/><path d="M3 6l9 7 9-7"/></svg>
<div class="abs f-col" style="left:645px"><div class="k">Email</div>info@tarvondinnovations.com</div>

<svg class="abs f-icon" style="left:914px" viewBox="0 0 24 24" fill="none" stroke="#fff" stroke-width="1.6"><path d="M6.6 10.8a15 15 0 0 0 6.6 6.6l2.2-2.2a1 1 0 0 1 1-.25 11.4 11.4 0 0 0 3.6.57 1 1 0 0 1 1 1V20a1 1 0 0 1-1 1A17 17 0 0 1 3 4a1 1 0 0 1 1-1h3.5a1 1 0 0 1 1 1c0 1.25.2 2.45.57 3.57a1 1 0 0 1-.25 1z"/></svg>
<div class="abs f-col" style="left:950px"><div class="k">Phone</div>+1 555-010-2040</div>

<div class="abs f-rule"></div>
<div class="abs copy">2024 Tarvond Innovations. All rights reserved</div>

</body>
</html>
```